Flyer Design Project

Painting and Maintenance
This is what I have as idea as Job description
Refresh, renew & revive your home. from painting to carpentry. Do you guys have any epic unique slogan?
As what we do Residential - Commercial Interior - ExteriorTrim & Molding installationWainscoting - Wallpaper removalCabinet refinishing Woodwork EnamelingDeck & Fence Cleaning & SealingPressure washConcrete & Paver Washing
I would like to have a note that says-Prompt professional service-Free estimates-Insured -"visit us on ChatHive"
I would like new ideas from you guys as well!
Carpentry

```html
<!DOCTYPE html>
<html lang="en">
<head>
<meta charset="utf-8">
<title>Painting &amp; Maintenance Flyer</title>
<link rel="stylesheet" href="https://fonts.googleapis.com/css2?family=Raleway:wght@400;700;800&display=swap">
<style>
  :root {
    --red: #d2392f;
    --white: #ffffff;
    --brick-dark: #6e4436;
    --brick: #94604d;
    --mortar: #a98270;
    --stair-light: #eef0f1;
    --stair-shade: #b9bfc3;
    --scaffold: #a4543b;
    --sky: #8fb3cf;
    --interior: #dfe4e8;
  }
  * { margin: 0; padding: 0; box-sizing: border-box; }
  html, body { width: 789px; height: 1200px; overflow: hidden; }
  body { font-family: "Raleway", sans-serif; color: var(--white); }

  .flyer {
    position: relative;
    width: 789px;
    height: 1200px;
    overflow: hidden;
  }
  .backdrop {
    position: absolute;
    inset: 0;
    background:
      linear-gradient(160deg, transparent 0 42%, var(--stair-shade) 42% 44%, var(--stair-light) 44% 100%),
      linear-gradient(180deg, var(--brick-dark) 0%, var(--brick) 40%, var(--mortar) 70%, var(--brick) 100%);
  }

  .section-title {
    position: absolute;
    left: 314px;
    font-weight: 700;
    font-size: 42px;
    letter-spacing: 0.5px;
    line-height: 1;
    text-shadow: 0 1px 3px rgba(0,0,0,0.25);
  }
  .services-title { top: 58px; }
  .promise-title { top: 670px; }

  .panel {
    position: absolute;
    background: var(--red);
    border-radius: 42px;
  }
  .services-panel {
    left: 206px;
    top: 95px;
    width: 514px;
    height: 457px;
    padding: 30px 0 0 108px;
  }
  .promise-panel {
    left: 50px;
    top: 709px;
    width: 674px;
    height: 244px;
    padding: 36px 0 0 95px;
  }

  .service-list, .promise-list { list-style: none; }
  .service-list li, .promise-list li, .promise-note {
    font-size: 20px;
    line-height: 34.3px;
    font-weight: 400;
  }
  .service-list li::before, .promise-list li::before { content: "• "; }
  .promise-note { width: 470px; }

  .photo {
    position: absolute;
    top: 981px;
    width: 286px;
    height: 181px;
    border: 4px solid var(--red);
    border-radius: 32px;
  }
  .photo-exterior {
    left: 50px;
    background: linear-gradient(180deg, var(--sky) 0%, var(--sky) 25%, var(--scaffold) 25%, #7d4534 100%);
  }
  .photo-interior {
    left: 438px;
    background: linear-gradient(135deg, #f7f8f9 0%, var(--interior) 55%, #9ea6ad 100%);
  }
</style>
</head>
<body>
  <main class="flyer">
    <div class="backdrop" role="img" aria-label="Brick wall behind bright white concrete stairs"></div>

    <h2 class="section-title services-title">OUR SERVICES</h2>
    <section class="panel services-panel">
      <ul class="service-list">
        <li>Residential to Commercial</li>
        <li>Interior to Exterior</li>
        <li>Trim &amp; Molding Installation</li>
        <li>Wainscoting</li>
        <li>Wallpaper Removal</li>
        <li>Cabinet Refinishing</li>
        <li>Woodwork</li>
        <li>Enameling</li>
        <li>Deck &amp; Fence</li>
        <li>Cleaning &amp; Sealing</li>
        <li>Pressure wash</li>
        <li>Concrete &amp; Paver Washing</li>
      </ul>
    </section>

    <h2 class="section-title promise-title">OUR PROMISE</h2>
    <section class="panel promise-panel">
      <ul class="promise-list">
        <li>Prompt Professional Service</li>
        <li>Free estimates</li>
        <li>Quality Ensured</li>
      </ul>
      <p class="promise-note">Visit us on ChatHive for more information or view some of our work.</p>
    </section>

    <div class="photo photo-exterior" role="img" aria-label="House exterior under renovation with scaffolding"></div>
    <div class="photo photo-interior" role="img" aria-label="Bright renovated kitchen and staircase interior"></div>
  </main>
</body>
</html>
```